Employee Benefits and Insurance Consulting

We are an existing company with over 30 years experience but are changing our name. We would like a simple design with grey tones.

Industry/Entity Type

Insurance

Contact Information for Business Card

Marlow Benefits Consulting
Gerald P Odell CEO
5172 Brackenfield Road
Louisville, TN 37777
gerald@marlowbx.com
865-412-3396 - O
865-247-5081 - C

```html
<!DOCTYPE html>
<html lang="en">
<head>
<meta charset="utf-8">
<title>Marlow Benefits Consulting – Business Card</title>
<link rel="stylesheet" href="https://fonts.googleapis.com/css2?family=Cinzel:wght@500&family=Roboto:wght@400;500&display=swap">
<style>
  :root {
    --backdrop: #e6e4e1;
    --card: #ffffff;
    --navy: #1f3f6e;
    --grey-text: #6d6f72;
    --shadow: rgba(0, 0, 0, 0.22);
  }
  html, body {
    margin: 0;
    padding: 0;
    width: 1200px;
    height: 1000px;
    overflow: hidden;
    background: var(--backdrop);
  }
  .canvas {
    position: relative;
    width: 1200px;
    height: 1000px;
  }
  .card {
    position: absolute;
    left: 265px;
    width: 666px;
    height: 397px;
    background: var(--card);
    box-shadow: 0 3px 8px var(--shadow);
  }
  .card--front { top: 73px; }
  .card--back { top: 532px; }

  .brand {
    position: absolute;
    text-align: center;
    font-family: "Cinzel", Georgia, serif;
    font-weight: 500;
    color: var(--navy);
  }
  .brand__mark {
    display: block;
    margin: 0 auto;
    background: var(--navy);
  }
  .brand__name {
    display: block;
    white-space: nowrap;
    line-height: 1;
  }
  .brand__sub {
    display: block;
    line-height: 1;
  }

  .card--front .brand { left: 0; right: 0; top: 86px; }
  .card--front .brand__mark { width: 104px; height: 104px; }
  .card--front .brand__name { font-size: 38px; margin-top: 66px; letter-spacing: 0.5px; }
  .card--front .brand__sub { font-size: 20px; margin-top: 10px; letter-spacing: 4px; }

  .card--back .brand { left: 40px; width: 284px; top: 108px; }
  .card--back .brand__mark { width: 88px; height: 88px; }
  .card--back .brand__name { font-size: 29px; margin-top: 50px; }
  .card--back .brand__sub { font-size: 16px; margin-top: 8px; letter-spacing: 3px; }

  .contact {
    position: absolute;
    left: 402px;
    top: 96px;
    font-family: "Roboto", Arial, sans-serif;
    color: var(--grey-text);
    font-size: 17px;
    line-height: 25px;
  }
  .contact__name {
    margin: 0;
    font-size: 20px;
    font-weight: 500;
    color: var(--navy);
    line-height: 24px;
  }
  .contact__title { margin: 0 0 21px; }
  .contact__address { margin: 0 0 11px; font-style: normal; }
  .contact__list { list-style: none; margin: 0; padding: 0; }
  .contact__list li {
    display: flex;
    align-items: center;
    gap: 9px;
    height: 25.5px;
  }
  .contact__icon {
    width: 16px;
    height: 16px;
    flex: none;
    fill: var(--navy);
  }
</style>
</head>
<body>
<main class="canvas">
  <section class="card card--front" aria-label="Card front">
    <div class="brand">
      <span class="brand__mark"></span>
      <span class="brand__name">MARLOW BENEFITS</span>
      <span class="brand__sub">CONSULTING</span>
    </div>
  </section>

  <section class="card card--back" aria-label="Card back">
    <div class="brand">
      <span class="brand__mark"></span>
      <span class="brand__name">MARLOW BENEFITS</span>
      <span class="brand__sub">CONSULTING</span>
    </div>

    <div class="contact">
      <p class="contact__name">Gerald P Odell</p>
      <p class="contact__title">CEO</p>
      <address class="contact__address">5172 Brackenfield Road<br>Louisville, TN 37777</address>
      <ul class="contact__list">
        <li>
          <svg class="contact__icon" viewBox="0 0 16 16" aria-hidden="true"><path d="M5 1h6a1 1 0 0 1 1 1v12a1 1 0 0 1-1 1H5a1 1 0 0 1-1-1V2a1 1 0 0 1 1-1zm1 2v6h4V3H6zm1 8v1h2v-1H7z"/></svg>
          <span>865-412-3396</span>
        </li>
        <li>
          <svg class="contact__icon" viewBox="0 0 16 16" aria-hidden="true"><path d="M1 5c0-1.5 3-3 7-3s7 1.5 7 3v1.5h-3.5V5h-7v1.5H1V5zm3 2.5h8l2 6.5H2l2-6.5zm4 1.5a2 2 0 1 0 0 4 2 2 0 0 0 0-4z"/></svg>
          <span>865-247-5081</span>
        </li>
        <li>
          <svg class="contact__icon" viewBox="0 0 16 16" aria-hidden="true"><path d="M1 4h14v9H1V4zm1.5 1.2V5.5L8 9.5l5.5-4V5.2H2.5zm0 2.1V11.8h11V7.3L8 11.2 2.5 7.3z"/></svg>
          <span>gerald@marlowbx.com</span>
        </li>
      </ul>
    </div>
  </section>
</main>
</body>
</html>
```